Book cover for publishing doctoral research about various national styles of piano playing.

I need a book cover for a publication of a doctoral research with regard to styles of piano performance characteristic to various nations.

Any images or graphics are optional, typography seems most important, but please feel free to be creative.

I attach the barcode, qsr and publisher's logo in the next few days. (Logo is still being designed).

For various reasons the size of the book is not completely decided yet. Please create your design in 7" x 10", but if at all possible, I would like to ask for files of two sizes, also including 8.5" x 11" in the final submission.

I am looking for a design that looks professional, probably simple, but I am open to any suggestions.

Dear Designers,I would like to thank you all for participation and submitting so many high-quality designs.My final decision was based on the feedback I received from my professional colleagues and potential readers.I would like to wish you all the best for the future.Best wishes,Tadeusz Added Monday, December 21, 2015

Pianists, students, music professionals

Publishing

• Title: Unfolding Seven Harbour Lullabies
• Subtitle: Memories and departures
• Author: Tadeusz Jarocki
• Space for my logo on the front page and the spine.
• On the back page, please include some space for a short biography, 'barcode' and 'qsr' code.
• Please include whatever else you consider necessary.
• Would it be possible to use the same cover to a e-book edition?

```html
<!DOCTYPE html>
<html lang="en">
<head>
<meta charset="utf-8">
<title>Unfolding Seven Harbour Lullabies — Tadeusz Jarocki</title>
<link rel="stylesheet" href="https://fonts.googleapis.com/css2?family=Oranienbaum&family=EB+Garamond&family=Open+Sans:wght@700&display=swap">
<style>
  :root {
    --backdrop: #f0efd9;
    --frame: #ffffff;
    --paper-light: #ead7b4;
    --paper-mid: #dcc198;
    --paper-edge: #b98e5c;
    --ink: #2a2623;
    --ink-soft: #6d6257;
    --piano-dark: #1f1b18;
    --piano-mid: #5b4f44;
  }
  * { margin: 0; padding: 0; box-sizing: border-box; }
  html, body {
    width: 900px; height: 1200px; overflow: hidden;
    background: var(--backdrop);
  }
  .cover {
    position: absolute; left: 76px; top: 24px;
    width: 748px; height: 1152px;
    border: 3px solid var(--frame);
    background:
      radial-gradient(ellipse at 50% 45%, var(--paper-light) 0%, var(--paper-mid) 62%, var(--paper-edge) 100%);
    overflow: hidden;
  }
  .publisher-mark {
    position: absolute; left: 330px; top: 42px;
    width: 86px; height: 86px; border-radius: 50%;
    border: 3px solid var(--ink);
    display: flex; align-items: center; justify-content: center;
    font-family: "Open Sans", sans-serif; font-weight: 700;
    font-size: 18px; color: var(--ink);
  }
  .title { font-weight: normal; }
  .title-main {
    position: absolute; left: 0; right: 0; top: 112px;
    text-align: center;
    font-family: "Oranienbaum", serif;
    font-size: 168px; line-height: 1;
    letter-spacing: -3px;
    color: var(--ink);
    transform: scaleX(0.62);
    transform-origin: 50% 50%;
  }
  .title-line {
    position: absolute; left: 0; right: 0; top: 294px;
    display: flex; justify-content: center; align-items: baseline; gap: 10px;
    font-family: "Oranienbaum", serif; color: var(--ink);
    transform: scaleX(0.86);
    transform-origin: 50% 50%;
  }
  .title-line .word { font-size: 60px; line-height: 1; letter-spacing: -1px; }
  .title-line .keyword {
    font-size: 30px; line-height: 1; color: var(--ink-soft);
  }
  .subtitle {
    position: absolute; left: 0; right: 0; top: 440px;
    text-align: center;
    font-family: "EB Garamond", serif; font-size: 24px;
    color: var(--ink);
  }
  .illustration {
    position: absolute; left: 158px; top: 538px;
    width: 432px; height: 446px;
    border-radius: 18px;
    background: linear-gradient(160deg, var(--piano-mid) 0%, var(--piano-dark) 70%);
    opacity: 0.85;
  }
  .author {
    position: absolute; left: 0; right: 0; top: 1014px;
    text-align: center;
    font-family: "Open Sans", sans-serif; font-weight: 700;
    font-size: 28px; letter-spacing: 8px;
    color: var(--piano-dark);
  }
</style>
</head>
<body>
  <main class="cover">
    <div class="publisher-mark">LOGO</div>

    <h1 class="title">
      <span class="title-main">Unfolding</span>
      <span class="title-line">
        <span class="word">Seven</span>
        <span class="keyword">HARBOUR</span>
        <span class="word">Lullabies</span>
      </span>
    </h1>

    <p class="subtitle">Memories and departures</p>

    <div class="illustration" role="img" aria-label="Engraved-style illustration of an open grand piano"></div>

    <p class="author">TADEUSZ JAROCKI</p>
  </main>
</body>
</html>
```